One page sales fact sheet for data consultancy company

We need a serious and professional looking 1-page fact sheet that we want to send over to potential clients via email.
The upper part should consists of a header, the client logo and 3 charts.
(1 chart with 5 datapoints / 1 chart with 3 bubbles and percentage in it, 1 chart with numbers and text)
In the lower part there should be some text description about our company and a big chart consisting of a table (see drawing).
See attached drawing to get a better understanding of the whole idea.
The fact sheet should be catchy but professional in the same way.
Colors your choice but classic, i.e. black/white/grey/blue
The contest winner can expect more work from us based on the winning design.
*Please note that the logo reflects our original logo style but is not our
actual company name for privacy reasons

```html
<!DOCTYPE html>
<html lang="en">
<head>
<meta charset="utf-8">
<title>Market Analysis Fact Sheet</title>
<link rel="stylesheet" href="https://fonts.googleapis.com/css2?family=Oswald:wght@500;600&family=Montserrat:wght@500;600;700;800&display=swap">
<style>
  :root{
    --blue:#0a7fd4;
    --blue-deep:#0b4f95;
    --blue-bright:#0897e8;
    --teal:#19c6d6;
    --ink:#111;
    --bar:#636363;
    --grid:#c9c9c9;
    --panel:#f1f1f1;
    --white:#fff;
  }
  *{box-sizing:border-box;margin:0;padding:0}
  html,body{width:973px;height:1200px;overflow:hidden;background:#f4f4f4}
  .sheet{position:relative;width:973px;height:1200px;overflow:hidden;
    background:linear-gradient(135deg,#e9e9e9 0%,#f7f7f7 45%,#ececec 100%);
    font-family:"Montserrat",sans-serif;color:var(--ink)}
  .abs{position:absolute}
  .shapes{position:absolute;left:0;top:0}
  .title{left:63px;top:42px;font-family:"Oswald",sans-serif;font-weight:600;font-size:60px;line-height:1;color:var(--white);letter-spacing:-0.3px;white-space:nowrap}
  .client{left:629px;top:66px;font-weight:600;font-size:29px;color:var(--blue-deep)}
  .axis-label{left:58px;width:40px;font-size:8.5px;font-weight:600;text-align:right;color:#222}
  .point{top:512px;width:80px}
  .point h3{font-family:"Oswald",sans-serif;font-weight:500;font-size:20px;color:var(--blue-bright);line-height:1.1}
  .point p{margin-top:12px;font-size:8.6px;line-height:13px;font-weight:500;color:#222}
  .types-title{left:560px;top:214px;font-weight:800;font-size:25px;letter-spacing:6.5px;color:var(--blue-deep)}
  .pct{width:110px;text-align:center;font-weight:800;font-size:30px;color:#151515}
  .stat{font-family:"Oswald",sans-serif;font-weight:600;font-size:30px;line-height:1;color:#111}
  .stat span{color:var(--blue-deep)}
  .about{left:68px;top:796px;width:838px;text-align:center;font-size:15.2px;line-height:21px;font-weight:500;color:#111}
  .brand{left:720px;top:888px;width:180px;text-align:right;font-weight:800;font-size:42px;letter-spacing:-1px;color:#111}
  .steps-title{left:67px;top:1106px;transform:rotate(-90deg);transform-origin:left top;font-weight:700;font-size:27px;line-height:1;letter-spacing:9px;color:var(--white);white-space:nowrap}
  .step-label{font-weight:600;font-size:15px;color:var(--white)}
  .level{left:624px;font-weight:700;font-size:22px;letter-spacing:5px;color:var(--white)}
  .level.top{font-size:28px;letter-spacing:5.5px}
  .art{position:absolute;border-radius:8px}
</style>
</head>
<body>
<div class="sheet">

  <svg class="shapes" width="973" height="1200" viewBox="0 0 973 1200">
    <defs>
      <linearGradient id="ring" x1="0" y1="0" x2="0" y2="1">
        <stop offset="0" stop-color="#1fd0d6"/>
        <stop offset="1" stop-color="#0a72d0"/>
      </linearGradient>
      <linearGradient id="disk" x1="0" y1="0" x2="1" y2="1">
        <stop offset="0" stop-color="#ececec"/>
        <stop offset="1" stop-color="#c4c4c4"/>
      </linearGradient>
      <linearGradient id="badge" x1="0" y1="0" x2="0" y2="1">
        <stop offset="0" stop-color="#1fd6d6"/>
        <stop offset="1" stop-color="#0a70cf"/>
      </linearGradient>
      <linearGradient id="band" x1="0" y1="0" x2="1" y2="0">
        <stop offset="0" stop-color="#0a72c8"/>
        <stop offset="1" stop-color="#0b93e6"/>
      </linearGradient>
    </defs>

    <!-- header band and client panel -->
    <polygon points="0,0 519,0 570,138 0,138" fill="var(--blue)"/>
    <polygon points="519,0 973,0 973,181 585,181 570,138" fill="var(--white)"/>

    <!-- bar chart -->
    <g class="bar-chart">
      <g stroke="var(--grid)" stroke-width="1">
        <line x1="95" y1="181" x2="520" y2="181"/>
        <line x1="95" y1="226" x2="520" y2="226"/>
        <line x1="95" y1="272" x2="520" y2="272"/>
        <line x1="95" y1="317" x2="520" y2="317"/>
        <line x1="95" y1="362" x2="520" y2="362"/>
        <line x1="95" y1="407" x2="520" y2="407"/>
        <line x1="95" y1="453" x2="520" y2="453"/>
        <line x1="95" y1="498" x2="520" y2="498"/>
      </g>
      <g fill="var(--bar)">
        <rect x="131" y="181" width="46" height="317"/>
        <rect x="210" y="292" width="46" height="206"/>
        <rect x="290" y="396" width="46" height="102"/>
        <rect x="369" y="339" width="46" height="159"/>
        <rect x="448" y="252" width="46" height="246"/>
      </g>
      <polyline points="95,167 95,609 520,609" fill="none" stroke="var(--blue-deep)" stroke-width="1.5"/>
    </g>

    <!-- product type rings -->
    <g class="rings">
      <g transform="translate(638 342)">
        <circle r="73" fill="#dcdcdc"/>
        <circle r="64" fill="none" stroke="url(#ring)" stroke-width="17" stroke-dasharray="160.8 402" transform="rotate(90)"/>
        <circle r="55" fill="url(#disk)"/>
      </g>
      <g transform="translate(834 342)">
        <circle r="73" fill="#dcdcdc"/>
        <circle r="64" fill="none" stroke="url(#ring)" stroke-width="17" stroke-dasharray="120.6 402" transform="rotate(90)"/>
        <circle r="55" fill="url(#disk)"/>
      </g>
      <g transform="translate(638 507)">
        <circle r="73" fill="#dcdcdc"/>
        <circle r="64" fill="none" stroke="url(#ring)" stroke-width="17" stroke-dasharray="80.4 402" transform="rotate(90)"/>
        <circle r="55" fill="url(#disk)"/>
      </g>
      <g transform="translate(834 507)">
        <circle r="73" fill="#dcdcdc"/>
        <circle r="64" fill="none" stroke="url(#ring)" stroke-width="17" stroke-dasharray="40.2 402" transform="rotate(90)"/>
        <circle r="55" fill="url(#disk)"/>
      </g>
    </g>

    <!-- stat pills -->
    <g class="stat-pills" fill="var(--panel)" stroke="#cfcfcf">
      <rect x="131" y="642" width="239" height="47"/>
      <rect x="131" y="722" width="404" height="48"/>
      <rect x="614" y="642" width="286" height="47"/>
      <rect x="614" y="722" width="286" height="48"/>
    </g>
    <g class="stat-badges">
      <circle cx="112" cy="666" r="36" fill="url(#badge)" stroke="#fff" stroke-width="3"/>
      <circle cx="112" cy="746" r="36" fill="url(#badge)" stroke="#fff" stroke-width="3"/>
      <circle cx="596" cy="666" r="36" fill="url(#badge)" stroke="#fff" stroke-width="3"/>
      <circle cx="596" cy="746" r="36" fill="url(#badge)" stroke="#fff" stroke-width="3"/>
      <g fill="none" stroke="#fff" stroke-width="2" stroke-linecap="round" stroke-linejoin="round">
        <circle cx="112" cy="656" r="5"/><circle cx="99" cy="660" r="4"/><circle cx="125" cy="660" r="4"/>
        <path d="M103 684v-12a9 9 0 0 1 18 0v12M92 684v-9a7 7 0 0 1 7-7M132 684v-9a7 7 0 0 0-7-7"/>
        <rect x="99" y="734" width="24" height="24"/>
        <path d="M104 746l6 6 14-16"/>
        <rect x="582" y="664" width="14" height="14"/><rect x="598" y="664" width="14" height="14"/><rect x="590" y="650" width="14" height="14"/>
        <path d="M580 758h32M584 752l8-8 6 5 12-13M604 736h6v6"/>
      </g>
    </g>

    <!-- bottom band with brand panel -->
    <polygon points="0,916 590,916 612,961 973,961 973,1200 0,1200" fill="url(#band)"/>

    <!-- arrows -->
    <g fill="#5fc8f5">
      <path d="M309 1031h14v-7l12 11-12 11v-7h-14z"/>
      <path d="M355 1031h14v-7l12 11-12 11v-7h-14z"/>
      <path d="M410 1031h14v-7l12 11-12 11v-7h-14z"/>
    </g>

    <!-- stairs -->
    <g fill="none" stroke-width="8">
      <polyline points="75,1200 75,1128 148,1128" stroke="#6cc24a"/>
      <polyline points="174,1170 174,1106 249,1106" stroke="#d4e04a"/>
      <polyline points="274,1146 274,1082 351,1082" stroke="#f4e84a"/>
      <polyline points="374,1112 374,1059 450,1059" stroke="#f5c52c"/>
      <polyline points="475,1084 475,1035 550,1035" stroke="#f5a21f"/>
    </g>
    <g>
      <polygon points="150,1120 160,1108 160,1120" fill="#6cc24a"/>
      <polygon points="251,1098 261,1086 261,1098" fill="#d4e04a"/>
      <polygon points="353,1074 363,1062 363,1074" fill="#f4e84a"/>
      <polygon points="452,1051 462,1039 462,1051" fill="#f5c52c"/>
    </g>

    <!-- label leaders -->
    <g stroke="#fff" stroke-width="1.2" fill="#fff">
      <line x1="578" y1="1060" x2="608" y2="1060"/><circle cx="608" cy="1060" r="1.8"/>
      <line x1="478" y1="1098" x2="608" y2="1098"/><circle cx="608" cy="1098" r="1.8"/>
      <line x1="370" y1="1132" x2="608" y2="1132"/><circle cx="608" cy="1132" r="1.8"/>
      <line x1="274" y1="1166" x2="608" y2="1166"/><circle cx="608" cy="1166" r="1.8"/>
    </g>
  </svg>

  <div class="art" role="img" aria-label="Illustration of a businessman with a briefcase running up the steps" style="left:192px;top:948px;width:106px;height:122px;background:linear-gradient(160deg,#3a6fc0,#1d3f8a)"></div>
  <div class="art" role="img" aria-label="Illustration of a gold trophy cup" style="left:466px;top:953px;width:82px;height:68px;background:linear-gradient(180deg,#ffc93a,#f19a12)"></div>

  <h1 class="abs title">MARKET ANALYSIS</h1>
  <div class="abs client">client logo/name</div>

  <div class="abs axis-label" style="top:176px">141-160</div>
  <div class="abs axis-label" style="top:221px">121-140</div>
  <div class="abs axis-label" style="top:267px">101-120</div>
  <div class="abs axis-label" style="top:312px">81-100</div>
  <div class="abs axis-label" style="top:357px">61-80</div>
  <div class="abs axis-label" style="top:402px">41-60</div>
  <div class="abs axis-label" style="top:448px">21-40</div>
  <div class="abs axis-label" style="top:493px">0-20</div>

  <div class="abs point" style="left:131px"><h3>Point 1</h3><p>Lorem ipsum<br>dolor sit amet,<br>consectetur</p></div>
  <div class="abs point" style="left:208px"><h3>Point 2</h3><p>Lorem ipsum<br>dolor sit amet,<br>consectetur</p></div>
  <div class="abs point" style="left:287px"><h3>Point 3</h3><p>Lorem ipsum<br>dolor sit amet,<br>consectetur</p></div>
  <div class="abs point" style="left:366px"><h3>Point 4</h3><p>Lorem ipsum<br>dolor sit amet,<br>consectetur</p></div>
  <div class="abs point" style="left:443px"><h3>Point 5</h3><p>Lorem ipsum<br>dolor sit amet,<br>consectetur</p></div>

  <h2 class="abs types-title">PRODUCT TYPES</h2>
  <div class="abs pct" style="left:583px;top:323px">40%</div>
  <div class="abs pct" style="left:779px;top:323px">30%</div>
  <div class="abs pct" style="left:583px;top:488px">20%</div>
  <div class="abs pct" style="left:779px;top:488px">10%</div>

  <div class="abs stat" style="left:176px;top:649px"><span>20</span> VENDOR</div>
  <div class="abs stat" style="left:176px;top:730px"><span>350,000</span> AVAILABLE ITEMS</div>
  <div class="abs stat" style="left:668px;top:649px"><span>750</span> PRODUCTS</div>
  <div class="abs stat" style="left:668px;top:730px"><span>40MLN</span> IN SALES</div>

  <p class="abs about">Lorem ipsum dolor sit amet, consectetur adipiscing elit, sed do eiusmod tempor incididunt ut labore et dolore magna aliqua. Ut enim ad minim veniam, quis nostrud exercitation ullamco laboris nisi ut aliquip ex ea commodo consequat. Duis aute irure dolor in reprehenderit in voluptate velit esse cillum</p>

  <div class="abs brand">Norvale</div>

  <div class="abs steps-title">STEPS</div>

  <div class="abs step-label" style="left:490px;top:1050px">LABEL 1</div>
  <div class="abs step-label" style="left:388px;top:1088px">LABEL 2</div>
  <div class="abs step-label" style="left:284px;top:1122px">LABEL 3</div>
  <div class="abs step-label" style="left:188px;top:1156px">LABEL 4</div>

  <div class="abs level top" style="top:1041px">COMPETITORS</div>
  <div class="abs level" style="top:1084px">USER LEVEL</div>
  <div class="abs level" style="top:1118px">ENTRY LEVEL</div>
  <div class="abs level" style="top:1152px">PERSONAL LEVEL</div>

</div>
</body>
</html>
```